Website Design Requirements

Domain Name: HometownTradesfolkRegistry.com

Website Look: Simple, Clean, Modern, and Professional Awarding Winning Website. Our Platform is the Best Directory Platform, all we need is a very creative person to make the following designs and select the fonts, font sizing, font colors and all the colors for the color points. We will follow up with the winner of the contest to design the rest of our design needs. The highlight of our brand is our Mascot; we feel this is something everyone will remember. It may be the easiest to obtain a free trial of the platform from Vantory Listings to complete this project. When we pick a winner of this contest we will provide the password to our admin panel for everything to be applied. Our Competitors are Perrows Hub, Yardwise Pro and Gravelnook.

We are thinking a light gray scale shadowing or graduated ghosting for the background behind the image of the Mascot for the main image. We want the Mascot and the Selection box to stand out as well as the logo.

Design Elements:
Main Page Image-Size for website is 1800 X 600px should be the Mascot on the right half of the image; this is where creative design is the most important. Design can use the head only from the waist up or the full image

Logo- Size for website is 450 X 70px; the logo should have the head of the mascot on a 3D icon with 2 line of text to the right side. The top line should have Hometown Tradesfolk the second line should have the word Directory in smaller size and be ghosted. The main idea about the logo is the icon and the words Hometown Tradesfolk. Note example can be seen on the Vantory Listings Rapid Launch Walkthrough on Clip Vue.

Favicon- Size for website is 56 X 56px should be the head of the mascot the Favicon and Google Map Pin drop could be the same if design is nice enough

Google Map Pin Drop- 25 X 46px should be the head of the mascot with a arrow pointing down.

Member Badge Image- Size 250 X 250px should be the head of the mascot inside a round ring with the words Verified –Certified –Member.

Target Market(s)

Consumers will use this website to locate Contractors in their Local area. Contractors will list their business on this website for a fee.

Industry/Entity Type

Domain

Contact Information for Business Card

Marcus Oldfield
Partner
555.014.2871
Marcus@HometownTradesfolkRegistry.Com
WWW. HometownTradesfolkRegistry.com

Logo Text

Hometown Tradesfolk Registry

Number of Pages Required

3 page

Font styles to use
Serif

Colors
ec1f27
fbed22

Requirements
Must have
• The use of our mascot, you can use full body view, waist up or head shot
Nice to have
• Clean bright colored Mascot, listing on back of card
• Hometown Tradesfolk
• Electricians
• Plumbers
• HVAC
• Landscapers
• General Contractors
• Garage Door Repair
• Carpet Cleaners
• Concrete Contractors

```html
<!DOCTYPE html>
<html lang="en">
<head>
<meta charset="utf-8">
<title>Hometown Tradesfolk Directory – Business Card</title>
<link rel="stylesheet" href="https://fonts.googleapis.com/css2?family=Alegreya:wght@500;700&display=swap">
<style>
  :root {
    --brand-red: #ec1f27;
    --deep-red: #b30f14;
    --brand-yellow: #fbed22;
    --card-yellow: #f3d91f;
    --ring-gold: #e8c21a;
    --text-light: #ffffff;
    --text-ghost: #f1e9e9;
    --text-dark: #1a1410;
  }
  * { margin: 0; padding: 0; box-sizing: border-box; }
  html, body {
    width: 1200px; height: 686px; overflow: hidden;
    background: #ddd;
  }
  .card {
    position: relative;
    width: 1200px; height: 686px; overflow: hidden;
    font-family: "Alegreya", Georgia, serif;
    background: var(--brand-red);
  }
  .interior-photo {
    position: absolute; inset: 0;
    background:
      radial-gradient(ellipse at 30% 85%, #d80e12 0%, transparent 55%),
      radial-gradient(ellipse at 55% 35%, #ff3a2e 0%, transparent 50%),
      linear-gradient(160deg, #ff1a10 0%, var(--brand-red) 45%, var(--deep-red) 100%);
  }
  .yellow-panel {
    position: absolute; inset: 0;
    width: 1200px; height: 686px;
  }
  .mascot-badge {
    position: absolute; left: 54px; top: 64px;
    width: 184px; height: 184px; border-radius: 50%;
    border: 5px solid var(--ring-gold);
    background: var(--deep-red);
    padding: 6px;
    box-shadow: 0 3px 10px rgba(0,0,0,.35);
  }
  .mascot-art {
    width: 100%; height: 100%; border-radius: 50%;
    background: radial-gradient(circle at 45% 40%, #f7f7f7 0%, #d9d9d9 55%, #a9a9a9 100%);
  }
  .brand-name {
    position: absolute; left: 262px; top: 86px;
    font-size: 72px; font-weight: 700; line-height: 1;
    color: var(--text-light);
    text-shadow: 0 3px 6px rgba(0,0,0,.35);
    white-space: nowrap;
  }
  .brand-sub {
    position: absolute; left: 262px; top: 172px;
    font-size: 50px; font-weight: 700; line-height: 1;
    color: var(--text-ghost);
    text-shadow: 0 3px 6px rgba(0,0,0,.3);
  }
  .contact-line {
    position: absolute; left: 82px;
    display: flex; align-items: center; gap: 12px;
    font-size: 32px; font-weight: 700; color: var(--text-light);
    text-shadow: 0 2px 4px rgba(0,0,0,.3);
    white-space: nowrap;
  }
  .contact-line svg { width: 42px; height: 38px; flex: none; }
  .contact-phone { top: 288px; }
  .contact-web { top: 336px; }
  .address {
    position: absolute; left: 694px; top: 568px;
    display: flex; align-items: center; gap: 14px;
  }
  .address svg { width: 44px; height: 66px; flex: none; }
  .address-lines {
    font-size: 32px; font-weight: 700; line-height: 34px;
    color: var(--text-dark);
    white-space: nowrap;
  }
</style>
</head>
<body>
<div class="card">
  <div class="interior-photo" role="img" aria-label="Living room interior photograph tinted red"></div>

  <svg class="yellow-panel" viewBox="0 0 1200 686" aria-hidden="true">
    <defs>
      <linearGradient id="panelGlow" x1="0" y1="0" x2="1" y2="1">
        <stop offset="0" stop-color="#fbe62a"/>
        <stop offset="1" stop-color="#efd51d"/>
      </linearGradient>
    </defs>
    <polygon points="1074,0 1200,0 1200,686 429,686" fill="url(#panelGlow)"/>
  </svg>

  <div class="mascot-badge">
    <div class="mascot-art" role="img" aria-label="Mascot: smiling contractor in a yellow hard hat"></div>
  </div>

  <div class="brand-name">Hometown Tradesfolk</div>
  <div class="brand-sub">Directory</div>

  <div class="contact-line contact-phone">
    <svg viewBox="0 0 42 38" aria-hidden="true">
      <path d="M3 12 Q21 0 39 12 L37 17 L29 15 L28 10 Q21 8 14 10 L13 15 L5 17 Z" fill="var(--brand-yellow)"/>
      <path d="M10 18 L32 18 L37 34 L5 34 Z" fill="var(--brand-yellow)"/>
      <circle cx="21" cy="26" r="5" fill="var(--brand-red)"/>
    </svg>
    <span>Contact Number</span>
  </div>

  <div class="contact-line contact-web">
    <svg viewBox="0 0 42 38" aria-hidden="true">
      <g fill="none" stroke="var(--brand-yellow)" stroke-width="2.2">
        <circle cx="26" cy="17" r="14"/>
        <ellipse cx="26" cy="17" rx="6" ry="14"/>
        <line x1="12" y1="17" x2="40" y2="17"/>
        <line x1="14" y1="10" x2="38" y2="10"/>
        <line x1="14" y1="24" x2="38" y2="24"/>
        <circle cx="12" cy="22" r="6" stroke-width="3"/>
      </g>
      <line x1="8" y1="27" x2="2" y2="35" stroke="var(--brand-yellow)" stroke-width="5" stroke-linecap="round"/>
    </svg>
    <span>HometownTradesfolkRegistry.com</span>
  </div>

  <div class="address">
    <svg viewBox="0 0 44 66" aria-hidden="true">
      <path d="M22 64 C14 46 3 36 3 22 A19 19 0 0 1 41 22 C41 36 30 46 22 64 Z" fill="var(--brand-red)" stroke="#9e0c10" stroke-width="1.5"/>
      <circle cx="22" cy="22" r="11" fill="var(--brand-yellow)"/>
    </svg>
    <div class="address-lines">
      <div>Business Address Line 1</div>
      <div>Business Address Line 1</div>
    </div>
  </div>
</div>
</body>
</html>
```